Medicaid and Nursing Home Planning Law Firm Needs Customizable Flyer

We need a flyer for The Delvecki Law Firm, P.C. that incorporates our logo, color scheme and existing collaterals (see uploads) and that can be easily updated. The flyer could advertise an upcoming speech/seminar/gathering, but the text should be customizable so that we can revise it later on using either MSWord or some other basic software.

Industry/Entity Type

Legal

Requirements
Must have
• Logo and contact information for business, including address, phone number, email and website information
Nice to have
• Also should advertise our 2nd location: 418 Brantley Avenue, Suite 305, Watertown, NY 13688

```html
<!DOCTYPE html>
<html lang="en">
<head>
<meta charset="UTF-8">
<title>The Delvecki Law Firm, P.C. – Flyer</title>
<link rel="stylesheet" href="https://fonts.googleapis.com/css2?family=Open+Sans:wght@300;400;600;700&display=swap">
<style>
  :root {
    --orange: #d6782b;
    --orange-deep: #c96c22;
    --ink: #3a3a3a;
    --grey-text: #555555;
    --white: #ffffff;
    --photo-dark: #2a1a14;
    --photo-mid: #7a5a3c;
    --photo-light: #d9c29b;
    --stone-light: #e4e3e2;
    --stone-mid: #b9b6b4;
  }
  * { margin: 0; padding: 0; box-sizing: border-box; }
  html, body { width: 850px; height: 1200px; overflow: hidden; background: var(--white); }
  body { font-family: "Open Sans", Arial, sans-serif; }

  .flyer { position: relative; width: 850px; height: 1200px; overflow: hidden; background: var(--white); }

  .hero-photo {
    position: absolute; left: 0; top: 0; width: 850px; height: 580px;
    background:
      radial-gradient(ellipse at 60% 35%, var(--photo-light) 0%, var(--photo-mid) 45%, transparent 75%),
      linear-gradient(180deg, var(--photo-dark) 0%, var(--photo-mid) 30%, #b99a70 60%, var(--photo-mid) 92%, var(--photo-dark) 100%);
  }

  .about {
    position: absolute; left: 0; top: 580px; width: 850px; height: 335px;
    background: var(--orange);
    border-bottom: 2px solid #e9b98f;
  }
  .about-rule {
    position: absolute; left: 68px; top: 87px; width: 4px; height: 225px;
    background: var(--white);
  }
  .about-title {
    position: absolute; left: 102px; top: 80px;
    color: var(--white); font-weight: 300; font-size: 44px; letter-spacing: 0.5px; line-height: 1;
  }
  .about-text {
    position: absolute; left: 102px; top: 144px; width: 700px;
    color: var(--white); font-weight: 400; font-size: 20.5px; line-height: 30px;
  }

  .services {
    position: absolute; left: 0; top: 917px; width: 542px; height: 283px;
    background: linear-gradient(160deg, var(--stone-light) 0%, #cfcdcb 45%, var(--stone-mid) 100%);
  }
  .services-title {
    position: absolute; left: 97px; top: 45px;
    color: var(--ink); font-size: 24px; font-weight: 400; letter-spacing: 0.3px;
  }
  .services-list { position: absolute; left: 103px; top: 88px; list-style: none; }
  .services-list li {
    position: relative; padding-left: 16px; height: 31.5px;
    font-size: 13.5px; font-weight: 600; color: var(--ink);
  }
  .services-list li::before {
    content: ""; position: absolute; left: 0; top: 6px; width: 6px; height: 6px;
    background: var(--orange);
  }

  .contact-panel {
    position: absolute; left: 542px; top: 917px; width: 308px; height: 283px;
    background: var(--white); text-align: center;
  }
  .brand { position: absolute; left: 0; top: 95px; width: 308px; }
  .brand-square {
    display: block; margin: 0 auto 14px; width: 22px; height: 22px; background: var(--grey-text);
  }
  .brand-name {
    font-size: 14px; font-weight: 400; letter-spacing: 2.5px; color: var(--grey-text);
  }
  .cta {
    position: absolute; left: 0; top: 204px; width: 308px;
    font-size: 14px; font-weight: 400; color: #222222;
  }
  .website {
    position: absolute; left: 0; top: 240px; width: 308px;
    font-size: 12px; font-weight: 700; letter-spacing: 1.5px; color: var(--orange-deep);
  }
</style>
</head>
<body>
<main class="flyer">
  <div class="hero-photo" role="img" aria-label="Close-up photograph of a Last Will and Testament document with a red pen resting on it"></div>

  <section class="about">
    <div class="about-rule"></div>
    <h2 class="about-title">ABOUT US</h2>
    <p class="about-text">The Delvecki Law Firm, P.C. was founded in 2015 to focus solely on planning for residents of Central and Northern New York with needs in Elder law/Medicaid planning, Estate Planning, Trust &amp; Estate Administration/Litigation, and Guardianship/Special Needs Planning areas.</p>
  </section>

  <section class="services" role="img" aria-label="Soft grey stone texture background behind the list of services">
    <h3 class="services-title">SERVICES WE OFFER</h3>
    <ul class="services-list">
      <li>Elder law</li>
      <li>Medicaid planning</li>
      <li>Estate Planning</li>
      <li>Trust &amp; Estate Administration</li>
      <li>Trust &amp; Estate Litigation</li>
      <li>Guardianship &amp; Special Needs Planning.</li>
    </ul>
  </section>

  <aside class="contact-panel">
    <div class="brand">
      <span class="brand-square"></span>
      <div class="brand-name">THE DELVECKI LAW FIRM</div>
    </div>
    <p class="cta">BOOK A FREE CONSULTATION NOW!</p>
    <p class="website">www.thedelveckilawfirm.com</p>
  </aside>
</main>
</body>
</html>
```